Thornbury Ridge & Beam Consultants- WEB DESIGN

I am seeking a more professional face to my current website.

www.TRBconsultants.com.au

Using same pages and same text, i need the pages to be presented in a more professional manner.

Use Same logo however all other items may be changed to make it look better... Main theme being a navy blue.

Project Deadline Extended
Reason: Alot of recent interest. Awaiting designs.

Target Market(s)

Engineers, Students, Public, Local Authorities, Draftsmen, Architects, Builders etc

Requirements
Must have
• Logo as per site,
• Navy Blue Theme,
• Professional feel,
• Images to attract eye and clients attention. (dont use large infrastructure yet more Residential designs, Crack inspections and Residential Construction)

```html
<!DOCTYPE html>
<html lang="en">
<head>
<meta charset="utf-8">
<title>Thornbury Ridge &amp; Beam Consultants</title>
<link rel="stylesheet" href="https://fonts.googleapis.com/css2?family=Montserrat:wght@700&family=Signika:wght@400;500&family=Noto+Sans:wght@400;700&display=swap">
<style>
  :root {
    --navy: #2b3990;
    --navy-dark: #24307c;
    --grey-heading: #555555;
    --grey-text: #444444;
    --card-border: #9a9a9a;
    --footer-bg: #d5dadb;
    --white: #ffffff;
    --ink: #111111;
  }
  * { margin: 0; padding: 0; box-sizing: border-box; }
  html, body { width: 1200px; height: 1034px; overflow: hidden; background: var(--white); }
  .page { position: relative; width: 1200px; height: 1034px; overflow: hidden; font-family: "Noto Sans", Verdana, sans-serif; color: var(--grey-text); }

  .brand-skyline {
    position: absolute; left: 432px; top: 8px; width: 352px; height: 106px;
    background: linear-gradient(180deg, #2a2a2a 0%, #5a5a5a 45%, #cfcfcf 55%, #ffffff 100%);
    border-radius: 2px;
  }
  .brand-name {
    position: absolute; left: 0; width: 1200px; text-align: center;
    font-family: "Montserrat", Arial, sans-serif; font-weight: 700; color: var(--navy);
  }
  .brand-name .primary { display: block; position: absolute; top: 122px; width: 100%; font-size: 48px; letter-spacing: 1px; line-height: 52px; }
  .brand-name .secondary { display: block; position: absolute; top: 177px; width: 100%; font-size: 20px; letter-spacing: 7px; line-height: 24px; }

  .service-card {
    position: absolute; top: 284px; width: 226px; height: 529px;
    border: 1px solid var(--card-border); border-radius: 12px; background: var(--white);
  }
  .service-card.structural { left: 114px; }
  .service-card.energy { left: 362px; }
  .service-card.inspections { left: 610px; }
  .service-card.construction { left: 859px; }

  .service-image { position: absolute; border-radius: 6px; }
  .structural .service-image { left: -6px; top: -14px; width: 236px; height: 224px; background: radial-gradient(ellipse at 35% 45%, #c9c3bb 0%, #e8e6e3 50%, #ffffff 80%); }
  .energy .service-image { left: 20px; top: -36px; width: 186px; height: 252px; background: radial-gradient(ellipse at 50% 55%, #8cc63f 0%, #cfe8b0 45%, #ffffff 78%); }
  .inspections .service-image { left: 0; top: -14px; width: 224px; height: 214px; background: radial-gradient(ellipse at 50% 45%, #d9642a 0%, #efc3a4 45%, #ffffff 78%); }
  .construction .service-image { left: 0; top: -14px; width: 224px; height: 246px; background: radial-gradient(ellipse at 50% 45%, #c8161d 0%, #ef9fa2 45%, #ffffff 78%); }

  .service-title {
    position: absolute; left: 19px; top: 233px; width: 200px; height: 54px;
    display: flex; align-items: flex-end;
    font-family: "Signika", Arial, sans-serif; font-weight: 500; font-size: 25px; line-height: 28px;
    color: var(--grey-heading); text-transform: uppercase;
  }
  .service-text {
    position: absolute; left: 20px; top: 306px; width: 190px;
    font-size: 11.6px; line-height: 17px; color: var(--grey-text);
  }
  .service-more {
    position: absolute; left: 20px; top: 454px;
    font-size: 13px; font-weight: 700; color: var(--grey-heading);
  }
  .service-action {
    position: absolute; left: 20px; top: 480px; width: 195px;
    font-size: 13px; line-height: 16.5px; font-weight: 700; color: var(--navy);
  }

  .contact-heading {
    position: absolute; left: 115px; top: 838px;
    font-family: "Signika", Arial, sans-serif; font-weight: 500; font-size: 19px; color: var(--navy);
  }
  .contact-details {
    position: absolute; left: 115px; top: 871px;
    font-family: "Signika", Arial, sans-serif; font-size: 14.5px; line-height: 21px; color: var(--ink);
  }
  .enquire-button {
    position: absolute; left: 610px; top: 842px; width: 476px; height: 67px;
    background: var(--navy); border-radius: 9px;
    display: flex; align-items: center; justify-content: center;
    font-family: "Signika", Arial, sans-serif; font-weight: 500; font-size: 25px; letter-spacing: 0.5px; color: var(--white);
  }

  .site-footer { position: absolute; left: 0; top: 931px; width: 1200px; height: 103px; background: var(--footer-bg); }
  .footer-nav {
    position: absolute; left: 114px; top: 31px;
    font-size: 12px; color: var(--navy);
  }
  .footer-nav .sep { margin: 0 4px; }
  .footer-legal { position: absolute; left: 114px; top: 56px; font-size: 9.5px; color: var(--grey-text); }
  .footer-badges { position: absolute; left: 824px; top: 26px; }
</style>
</head>
<body>
<div class="page">
  <header>
    <div class="brand-skyline" role="img" aria-label="City skyline with reflection above the company name"></div>
    <h1 class="brand-name">
      <span class="primary">THORNBURY</span>
      <span class="secondary">RIDGE &amp; BEAM CONSULTANTS</span>
    </h1>
  </header>

  <main>
    <section class="service-card structural">
      <div class="service-image" role="img" aria-label="3D house model over architectural floor plans"></div>
      <h2 class="service-title">Structural Engineering</h2>
      <p class="service-text">Structural and civil engineering for services for architects, building contractors, developers, local council and government bodies working on commercial, residential, industrial, and government buildings.</p>
      <p class="service-more">More info...</p>
      <p class="service-action">Submit details of your construction project</p>
    </section>

    <section class="service-card energy">
      <div class="service-image" role="img" aria-label="Green grass-roofed house with a sprouting plant"></div>
      <h2 class="service-title">Energy Rating</h2>
      <p class="service-text">We will provide a free Energy Rating on residential structural designs until the end of the month to ensure your energy performance complies with the minimum 6-Star rating required for all new homes and apartments in Victoria.</p>
      <p class="service-more">More info...</p>
      <p class="service-action">Enquire online about your free Energy Rating</p>
    </section>

    <section class="service-card inspections">
      <div class="service-image" role="img" aria-label="House under construction with timber frame and orange roof"></div>
      <h2 class="service-title">House Inspections</h2>
      <p class="service-text">For your peace-of-mind. Pre-purchase inspections to assess the structural condition of your chosen property, building inspections throughout all stages of new home construction and forensic investigation and reporting.</p>
      <p class="service-more">More info...</p>
      <p class="service-action">Register for an inspection online today</p>
    </section>

    <section class="service-card construction">
      <div class="service-image" role="img" aria-label="Red house built from blocks with loose cubes"></div>
      <h2 class="service-title">Construction Services</h2>
      <p class="service-text">With more than 25 years experience and and pride in our work, we offer innnovative design solutions incorporating our up-to-date knowledge of new and emerging construction trends. Let us turn your vision into reality.</p>
      <p class="service-more">More info...</p>
      <p class="service-action">Upload working drawings for a building proposal</p>
    </section>

    <h3 class="contact-heading">GET IN TOUCH...</h3>
    <p class="contact-details">Mobile: 0400 555 218 | Email: admin@trbconsultants.com.au<br>Head Office: 22 Calder Lane, Thornbury Victoria 3071 Australia</p>
    <div class="enquire-button">ENQUIRE ONLINE NOW</div>
  </main>

  <footer class="site-footer">
    <nav class="footer-nav">
      Structural Engineering<span class="sep">|</span>Energy Rating<span class="sep">|</span>House Inspections<span class="sep">|</span>Construction Services<span class="sep">|</span>Contact Us<span class="sep">|</span>Register
    </nav>
    <p class="footer-legal">Copyright 2013 Thornbury Ridge &amp; Beam Consultants | Terms of Use</p>
    <svg class="footer-badges" width="262" height="56" viewBox="0 0 262 56" aria-label="Membership and registration badges">
      <rect x="0" y="0" width="35" height="55" rx="2" fill="#1b8fd6"/>
      <rect x="68" y="12" width="36" height="40" fill="#e2231a"/>
      <circle cx="116" cy="31" r="13" fill="none" stroke="#777" stroke-width="2"/>
      <rect x="134" y="24" width="72" height="14" fill="#8a8a8a"/>
      <rect x="222" y="1" width="40" height="52" rx="8" fill="#1f7a3a"/>
    </svg>
  </footer>
</div>
</body>
</html>
```